Brenmoor Systems Website Revamp

We need a full website for the oil and gas sector to showcase our company and our technology/services we provide to larger corporations. We want our website represent innovation and identity.

Background:

We are a service based company that specializes in:

- well services, and
-permanent applications
**(Please be aware that these are two different aspects to the oil and gas sector, both of which we supply to our customers)

We provide a wide range of jet pump technologies to address under performing reservoirs or problematic well producing conditions. We have field operations currently in: Canada, Oman, and Australia with efforts currently underway to expand in other markets. Therefore are needing a website to help promote a better comprehension of what we do and how we can solve their well issues. We are looking for

1.) Identity;
2.) Emphasis on better comprehension of our services for our clients to relate to us as a solution to their needs;
3.) User friendly interface - but new and exciting in this digital age .

Some examples of websites we like:

http://quorvalinc.com/how-we-work/
http://www.tandrisystems.com/tandri-system/
https://mirelfield.com/

Videos of our technologies:

https://www.vidoquay.com/watch?v=Qm47TzxR2pa
https://www.vidoquay.com/watch?v=Lk8WnbeT5yc

Target Market(s)

Petroleum Industry Clients

Coding

Coded - Design and coding required

Number of Pages Required

5+ page

Colors

Designer to choose colors to be used in the design.

Requirements
Must have
• See Project Description, and feel free to contact us with any questions/inquiries!
Nice to have
• Our color scheme is generally 'blue', to depict jet pumps (our service). However, we are open to ideas and artistic interpretation. Grayscale/offset colors/highlight colors etc.

```html
<!DOCTYPE html>
<html lang="en">
<head>
<meta charset="utf-8">
<title>Brenmoor Systems</title>
<link rel="stylesheet" href="https://fonts.googleapis.com/css2?family=Audiowide&family=Roboto:wght@400;500;700&family=Open+Sans:wght@400;700&display=swap">
<style>
:root{
  --dark:#1f1f21;
  --footer:#181819;
  --blue:#1f86dc;
  --blue-deep:#1c62c6;
  --blue-light:#23a2e6;
  --text:#222;
  --muted:#777;
  --pale:#f1f2f4;
  --white:#fff;
}
*{box-sizing:border-box;margin:0;padding:0}
html,body{width:1200px;height:2557px;overflow:hidden;background:var(--white)}
body{font-family:"Roboto",sans-serif;color:var(--text)}
.page{position:relative;width:1200px;height:2557px;overflow:hidden}
.abs{position:absolute}
.topbar{left:0;top:0;width:1200px;height:38px;background:var(--dark);color:#ddd;font-size:14px}
.topbar .contact{left:99px;top:11px;display:flex;gap:22px;align-items:center}
.topbar .contact span{display:flex;align-items:center;gap:9px}
.topbar .social{right:99px;top:11px;display:flex;gap:10px;align-items:center}
.topbar .social i{display:block;width:13px;height:13px;border-radius:50%;background:#e6e6e6}
.header{left:0;top:38px;width:1200px;height:103px;background:var(--white)}
.brand{display:flex;align-items:center;gap:10px;font-family:"Roboto",sans-serif;font-weight:700;font-size:24px;color:#1b1b1b}
.brand .dot{width:16px;height:16px;border-radius:50%;background:var(--blue)}
.header .brand{left:99px;top:36px}
.nav{right:99px;top:42px;display:flex;gap:28px;font-weight:700;font-size:16px;color:#222}
.hero{left:0;top:141px;width:1200px;height:590px;background:linear-gradient(180deg,#3a3b45 0%,#a65a2c 20%,#d98932 30%,#6b5c55 45%,#454850 65%,#2f3137 100%)}
.hero-title{left:639px;top:312px;font-family:"Audiowide",sans-serif;font-size:42px;color:var(--white)}
.hero-text{left:639px;top:376px;width:470px;font-size:15px;font-weight:500;line-height:24px;color:var(--white)}
.btn{display:inline-flex;align-items:center;justify-content:center;gap:6px;border-radius:22px;font-weight:700;font-size:15px}
.btn-blue{background:linear-gradient(180deg,var(--blue-light),var(--blue-deep));color:var(--white)}
.btn-white{background:var(--white);color:var(--blue)}
.hero .btn{left:639px;top:311px;width:156px;height:43px}
.pager{left:523px;top:628px;display:flex;gap:8px;align-items:center}
.pager .ring{width:16px;height:16px;border:2px solid #fff;border-radius:50%}
.pager .ring.on{background:#fff}
.challenge{left:0;top:716px;width:1200px;height:760px;background:linear-gradient(180deg,#eceef1,#f3f4f6 60%,#eef0f3)}
.ghost{font-family:"Audiowide",sans-serif;color:rgba(120,120,130,.18);font-size:56px;letter-spacing:2px;white-space:nowrap;text-align:center;width:1200px;left:0}
.sec-title{font-family:"Audiowide",sans-serif;font-size:36px;text-align:center;width:1200px;left:0}
.challenge-text{left:200px;top:872px;width:800px;text-align:center;font-size:13px;line-height:24px;color:#555}
.divider{left:99px;top:1117px;width:1002px;height:1px;background:#d4d6da}
.feature{top:1186px;width:250px;text-align:center}
.feature svg{display:block;margin:0 auto}
.feature h3{margin-top:22px;font-size:21px;font-weight:500;color:#222}
.feature p{margin-top:14px;font-size:13px;line-height:23px;color:var(--muted)}
.solution-bg{left:0;top:1470px}
.solution-photo{left:109px;top:1640px;width:453px;height:288px;border:3px solid #fff;background:linear-gradient(160deg,#8b9a7a 0%,#9aa3a8 35%,#c23a2a 60%,#8a2a20 80%,#a8a6a2 100%)}
.sol-head{left:603px;top:1630px;font-family:"Open Sans",sans-serif;font-weight:700;font-size:28px;color:var(--white)}
.sol-text{left:603px;top:1692px;width:500px;font-family:"Open Sans",sans-serif;font-size:13px;line-height:23px;color:var(--white)}
.sol-text p+p{margin-top:12px}
.dashes{left:520px;top:1989px;display:flex;gap:14px}
.dashes i{display:block;width:30px;height:3px;background:rgba(255,255,255,.8)}
.dashes i.on{background:#10305e}
.col-head{top:2167px;font-size:18px;font-weight:500;color:#222;letter-spacing:.3px}
.ops{left:99px;top:2208px;list-style:none;font-size:14px;color:#444}
.ops li{display:flex;align-items:center;gap:12px;height:27px}
.ops li::before{content:"";width:11px;height:11px;border-radius:50%;background:var(--blue)}
.contact-list{left:389px;top:2208px;width:280px}
.c-item{display:flex;gap:18px;margin-bottom:20px;font-size:14px;line-height:23px;color:#555}
.c-icon{flex:none;width:36px;height:36px;border-radius:50%;background:#fff;box-shadow:0 1px 5px rgba(0,0,0,.12);display:flex;align-items:center;justify-content:center}
.c-item b{color:#333;font-weight:700}
.map{left:728px;top:2170px;width:373px;height:216px;border:4px solid #fff;box-shadow:0 1px 6px rgba(0,0,0,.15);background:linear-gradient(135deg,#d7e2c4,#ece8dc 50%,#e6e2d6)}
.map-btn{left:736px;top:2178px;background:#fff;padding:6px 12px;font-size:13px;font-weight:500;color:#222;box-shadow:0 1px 3px rgba(0,0,0,.2)}
.footer{left:0;top:2455px;width:1200px;height:102px;background:var(--footer)}
.footer .brand{left:99px;top:38px;color:#f2f2f2}
.copy{left:480px;top:42px;font-size:14px;color:#ddd}
.f-social{left:866px;top:32px;display:flex;gap:11px}
.f-social i{display:block;width:38px;height:38px;border:2px solid #ddd;border-radius:50%}
</style>
</head>
<body>
<div class="page">

  <div class="abs topbar">
    <div class="abs contact">
      <span><svg width="12" height="12" viewBox="0 0 24 24"><path fill="#ddd" d="M6.6 10.8a15 15 0 0 0 6.6 6.6l2.2-2.2c.3-.3.7-.4 1-.2 1.1.4 2.3.6 3.6.6.6 0 1 .4 1 1V20c0 .6-.4 1-1 1A17 17 0 0 1 3 4c0-.6.4-1 1-1h3.5c.6 0 1 .4 1 1 0 1.3.2 2.5.6 3.6.1.3 0 .7-.2 1z"/></svg>(+1) 555 014 2290</span>
      <span style="color:#888">|</span>
      <span><svg width="13" height="11" viewBox="0 0 24 18"><path fill="#ddd" d="M0 0h24v2L12 10 0 2zM0 4l12 8 12-8v14H0z"/></svg>info@brenmoorsystem.com</span>
    </div>
    <div class="abs social">Stay Conneted: <i></i><i></i><i></i><i></i><i></i></div>
  </div>

  <header class="abs header">
    <div class="abs brand"><span class="dot"></span>Brenmoor Systems</div>
    <nav class="abs nav"><span>HOME</span><span>WHAT WE DO</span><span>WHO WE ARE</span><span>PRODUCT &amp; SERVICES</span><span>CONTACT US</span></nav>
  </header>

  <section class="abs hero" role="img" aria-label="Jet pump unit with electric motor at an oil field site at sunset">
    <h1 class="abs hero-title" style="top:171px">Jet Pump System</h1>
    <p class="abs hero-text" style="top:235px">Nemo enim ipsam voluptatem quia voluptas sit aspernatur aut odit aut fugit sed quia consequuntur magni dolores eos.</p>
    <a class="abs btn btn-blue">READ MORE <svg width="13" height="13" viewBox="0 0 16 16"><circle cx="8" cy="8" r="8" fill="#fff"/><path d="M6 4l4 4-4 4" stroke="#1f86dc" stroke-width="2" fill="none"/></svg></a>
    <div class="abs pager" style="top:487px">
      <svg width="14" height="20"><path d="M11 2L3 10l8 8" stroke="#fff" stroke-width="3" fill="none"/></svg>
      <span class="ring"></span><span class="ring on"></span><span class="ring"></span><span class="ring"></span>
      <svg width="14" height="20"><path d="M3 2l8 8-8 8" stroke="#fff" stroke-width="3" fill="none"/></svg>
    </div>
  </section>

  <section class="abs challenge" role="img" aria-label="Faint background of pumping machinery">
  </section>
  <svg class="abs" style="left:0;top:660px" width="1200" height="80" viewBox="0 0 1200 80">
    <path d="M0 8 Q600 95 1200 30 L1200 80 L0 80Z" fill="#eceef1"/>
    <path d="M0 8 Q600 95 1200 30 L1200 46 Q600 100 0 22Z" fill="#1f86dc"/>
  </svg>

  <div class="abs ghost" style="top:790px">THE CHALLENGE</div>
  <h2 class="abs sec-title" style="top:798px">The Challenge</h2>
  <p class="abs challenge-text">Lorem ipsum dolor sit amet, consectetur adipiscing elit, sed do eiusmod tempor incididunt ut labore et dolore magna aliqua. Ut enim ad minim veniam, quis nostrud exercitation ullamco laboris nisi ut aliquip ex ea commodo consequat. Duis aute irure dolor in reprehenderit in voluptate velit esse cillum dolore eu fugiat nulla pariatur. Excepteur sint occaecat cupidatat non proident ut aliquip sunt in eu fugiat culpa qui officia deserunt mollit anim id est laborum.</p>
  <a class="abs btn btn-blue" style="left:518px;top:999px;width:164px;height:43px">READ MORE <svg width="13" height="13" viewBox="0 0 16 16"><circle cx="8" cy="8" r="8" fill="#fff"/><path d="M6 4l4 4-4 4" stroke="#1f86dc" stroke-width="2" fill="none"/></svg></a>
  <div class="abs divider"></div>

  <div class="abs feature" style="left:88px">
    <svg width="76" height="72" viewBox="0 0 76 72" fill="none" stroke="#1f86dc" stroke-width="2.5"><circle cx="46" cy="24" r="14"/><path d="M40 38v8h12v-8M42 52h8"/><path d="M46 4V0M64 22h6M28 22h-4M60 10l4-4M32 10l-4-4"/><rect x="6" y="44" width="24" height="22" rx="3"/><circle cx="14" cy="54" r="2"/><circle cx="22" cy="54" r="2"/></svg>
    <h3>Permanent Artificial</h3>
    <p>Nemo enim voluptatem voluptas<br>sit aspernatur aut odit aut fugit sed quia<br>come sequuntur magni dolores</p>
  </div>
  <div class="abs feature" style="left:347px">
    <svg width="76" height="72" viewBox="0 0 76 72" fill="none" stroke="#1f86dc" stroke-width="2.5"><path d="M14 4l3 6 6 1-4 4 1 6-6-3-6 3 1-6-4-4 6-1zM38 2l3 6 6 1-4 4 1 6-6-3-6 3 1-6-4-4 6-1zM62 4l3 6 6 1-4 4 1 6-6-3-6 3 1-6-4-4 6-1z"/><path d="M10 40h12v28H10zM22 44l10-14c3-4 8-2 7 3l-2 9h18c4 0 5 4 3 6 2 2 1 5-1 6 1 2 0 5-2 6 1 3-1 6-4 6H22"/></svg>
    <h3>Well Services</h3>
    <p>Nemo enim voluptatem voluptas<br>sit aspernatur aut odit aut fugit sed quia<br>come sequuntur magni dolores</p>
  </div>
  <div class="abs feature" style="left:603px">
    <svg width="76" height="72" viewBox="0 0 76 72" fill="none" stroke="#1f86dc" stroke-width="2.5"><path d="M38 56C26 40 20 30 20 22a18 18 0 0 1 36 0c0 8-6 18-18 34z"/><circle cx="38" cy="22" r="8"/><path d="M24 50L6 62l32 8 32-8-18-12"/></svg>
    <h3>Locations</h3>
    <p>Nemo enim voluptatem voluptas<br>sit aspernatur aut odit aut fugit sed quia<br>come sequuntur magni dolores</p>
  </div>
  <div class="abs feature" style="left:860px">
    <svg width="76" height="72" viewBox="0 0 76 72" fill="none" stroke="#1f86dc" stroke-width="2.5"><rect x="36" y="4" width="34" height="24"/><path d="M36 4l17 14 17-14"/><path d="M12 30l8-6 8 10-5 5c3 7 8 12 15 15l5-5 10 8-6 8C28 66 8 46 12 30z"/></svg>
    <h3>Contact Us</h3>
    <p>Nemo enim voluptatem voluptas<br>sit aspernatur aut odit aut fugit sed quia<br>come sequuntur magni dolores</p>
  </div>

  <svg class="abs solution-bg" width="1200" height="610" viewBox="0 0 1200 610">
    <defs><linearGradient id="solBlue" x1="0" y1="0" x2="1" y2="0"><stop offset="0" stop-color="#1f9de3"/><stop offset="1" stop-color="#1d60c7"/></linearGradient></defs>
    <path d="M0 62 Q600 -55 1200 62 L1200 540 Q600 660 0 540Z" fill="url(#solBlue)"/>
  </svg>
  <div class="abs ghost" style="top:1546px;color:rgba(255,255,255,.22)">THE SOLUTION</div>
  <h2 class="abs sec-title" style="top:1550px;color:#fff">The Solution</h2>
  <div class="abs solution-photo" role="img" aria-label="Red electric pump units connected to grey pipework outdoors"></div>
  <h3 class="abs sol-head">Horizontal &amp; Deviated Wells</h3>
  <div class="abs sol-text">
    <p>With no moving parts, the BRX jet pump takes the industry to the next level, allowing for jet pump placement anywhere in the horizontal profile.</p>
    <p>Using power fluid as the drive mechanism of a jet pump, the system has no problems with deviated, crooked or horizontal wellbores. With a jet pump landed in the horizontal section of a well, operators are not only able to achieve higher inflow rates, they are also able to achieve higher ultimate reserve recovery.</p>
  </div>
  <a class="abs btn btn-white" style="left:603px;top:1884px;width:158px;height:44px">READ MORE <svg width="13" height="13" viewBox="0 0 16 16"><circle cx="8" cy="8" r="8" fill="#1f86dc"/><path d="M6 4l4 4-4 4" stroke="#fff" stroke-width="2" fill="none"/></svg></a>
  <svg class="abs" style="left:34px;top:1758px" width="34" height="52"><path d="M30 2L6 26l24 24" stroke="#fff" stroke-width="4" fill="none"/></svg>
  <svg class="abs" style="left:1132px;top:1758px" width="34" height="52"><path d="M4 2l24 24L4 50" stroke="#fff" stroke-width="4" fill="none"/></svg>
  <div class="abs dashes"><i></i><i></i><i class="on"></i><i></i></div>

  <h4 class="abs col-head" style="left:99px">AREA OF OPERATIONS</h4>
  <ul class="abs ops"><li>Sales</li><li>Engineering</li><li>Operations</li><li>Services</li><li>Acounting</li><li>Administration</li><li>Well Analysis</li></ul>

  <h4 class="abs col-head" style="left:389px">CONTACT US</h4>
  <div class="abs contact-list">
    <div class="c-item"><span class="c-icon"><svg width="12" height="16" viewBox="0 0 12 16"><path fill="#1f86dc" d="M6 0a6 6 0 0 1 6 6c0 4-6 10-6 10S0 10 0 6a6 6 0 0 1 6-6zm0 3.5a2.5 2.5 0 1 0 0 5 2.5 2.5 0 0 0 0-5z"/></svg></span><span>47 Ridgeway Lane, Calder Point,<br>North Vale, UK 4471</span></div>
    <div class="c-item"><span class="c-icon"><svg width="14" height="14" viewBox="0 0 24 24"><path fill="#1f86dc" d="M6.6 10.8a15 15 0 0 0 6.6 6.6l2.2-2.2c.3-.3.7-.4 1-.2 1.1.4 2.3.6 3.6.6.6 0 1 .4 1 1V20c0 .6-.4 1-1 1A17 17 0 0 1 3 4c0-.6.4-1 1-1h3.5c.6 0 1 .4 1 1 0 1.3.2 2.5.6 3.6.1.3 0 .7-.2 1z"/></svg></span><span><b>Phone:</b><br>403.555.0148 - 1.844.BRN.MOOR</span></div>
    <div class="c-item"><span class="c-icon"><svg width="14" height="11" viewBox="0 0 24 18"><path fill="#1f86dc" d="M0 0h24v2L12 10 0 2zM0 4l12 8 12-8v14H0z"/></svg></span><span><b>Email:</b><br>info@brenmoorsystem.com</span></div>
  </div>

  <div class="abs map" role="img" aria-label="Road map of the central United States with a red location marker"></div>
  <div class="abs map-btn">Get Direction ↱</div>

  <footer class="abs footer">
    <div class="abs brand"><span class="dot"></span>Brenmoor Systems</div>
    <div class="abs copy">© Brenmoor Systems 2018. All Right Reserved.</div>
    <div class="abs f-social"><i></i><i></i><i></i><i></i><i></i></div>
  </footer>

</div>
</body>
</html>
```